Online travel site needs edgy website design

tripnook is the first Global Business Travel Website that provides the most comprehensive destination information tailored to suit the business traveller.

It is a ‘one click solution’ that offers direct access to all aspects of business travel, including general information on the city, accommodation and transportation options, economic and financial statistics, key business and services contacts, as well as leisure activities, entertainment suggestions, and listings for any personal needs.

Much more than a travel website, tripnook.com eliminates the need to buy multiple travel books or visit scores of websites. Most importantly, it is the only website that will cover such an extensive range of destinations around the world, while also featuring cities where information is really scarce. The user-friendly and consistent format for all destinations will allow the business traveller to easily navigate through more than 100 information pages on any destination.

tripnook will be simple to navigate, intuitive, unique in design, dynamic, and content rich providing a supreme user experience during navigation of the website.

The website will initially be English and is set to expand to more languages in the future.

A beta site with back-end database has been built - and now we need an edgy state of the art graphic design to reskin it.

LOOK & FEEL

Scope
The design of the site should reflect tripnook’s corporate and user centric philosophy with the following elements:

a. tripnook corporate image and branding
b. the promotion of each city destination
c. tripnook being the starting point of travel, while also a partner during travel
d. the subtle but powerful presence of advertising and sponsorship

All the above must derive from the design outline and elements that are going to be used.

Design Guidelines

Innovative and elegant design, minimalism, simplicity that permits the offering of the required information to be delivered in line with the values of Trust, Care, Discovery & Connection.

In addition:

1. The usability, navigation and the informative character of the corporate web site should not be compromised by the design.
2. The over-segmented pages and over-crowded content per page should be avoided.
3. The design should not only guide the user in an inviting way to the information required but also to intrigue them for further navigation.
4. Advertising space should be anticipated in line with the design character and OMR standard ad sizes.
5. The use of photos / videos should also encouraged.

Key Elements

a. Branding/Logos
Throughout the website branding should be present as a “guarantee seal” for the content accuracy. Corporate logo should be placed on every page while branding should also characterise any content element and/or tool. Appendix contains the current brand guidelines. Should additional sub-logos be required for specific sections, these should be proposed.

b. Fonts
Provided your experience on the website design you are requested to propose alternative font types and sizes always taken into consideration the inviting and user friendly character that the new website should aspire to. The font type that will be proposed must be user friendly in English typography, but also could support other languages in the future.

Given the fact that the majority of the text in the website contains information and listing, the fonts and text layout should not strain and fatigue the reader.

c. SEO
The design should be friendly towards the search engines.

d. Colours
Colour is considered as an integral part of the brand identity. Tripnook.com corporate colours are orange and grey as per the Attached document reference guide.

Different tonalities of the brand colours, or colours in general, should be proposed and applied, guided always by the above described scope of Look & Feel.

e. Section Headings
As presented above, the site’s section headings (refer Overview of the Site.) The principle is to label the content following users’ needs and mindset. However, the label space should be flexible for changes. The labels should facilitate the user to understand the content they host. This is important and should be applied especially to informative content.

Another function that Headings should perform is that of promoting the website’s content, especially when this kind of content will make the user spend more time in the website. This category of Headings should be approached in a more creative and attractive way as to intrigue users to check the content hosted.

f. Icons
Icons are considered necessary in order to provide the user extra help to guide them to reach the information they need quick n’ easy. Icons not only contribute actively to the creation of an attractive look & feel but, most importantly, facilitate navigation and speed up the users’ familiarisation with the website too.

Therefore their design should be eye-catching, comprehensive and dynamic, in accordance to the new site’s colour coding and following the latest trends as these were defined by the look & feel of smart phones.

PIXELHIVE BRIEF REQUIREMENTS
Based on the above, please provide at least two (2) approaches for the following pages – this includes colour palette in line with logo, layout, fonts.

Initial submissions can just address Deliverable 1 & 2 to fine tune design before proceeding further.

Please refer sample screenshots separately attached from raw beta site for content – available for Deliverables 2 -6.

(REFER example sites we like for their creativity: http://www.quillark-studio.co.uk/#Background, http://www.pelorafestas.com.br/, http://brambletondesign.co.uk/ )

Deliverable 1: Landing /Home page
- Access log in –
o Free Account or via WorkLattice/Chatterly etc
o Membership Access – Login
- How to use the site
- Allowance for video or animation
- Destination Selection
- Blog & Social media links

Deliverable 2: Destination Landing Page / Template
This is essentially a city guide template to be used for all cities throughout the site.

This page clearly depicts the four information sections
1. General
2. Business
3. Leisure
4. Personal

Also this page should include:
- Business News Feed
- Advertising & Sponsorship Spaces (according to OMR Standards)
- Destination Time, Weather, FX rates (LIVE feeds)
- Tips

Deliverable 3: Follow the above format but show an Internal Content Page – text only with subheadings

Deliverable 4: Follow the above format but show an Internal Content Page – text and photos

Deliverable 5: Follow the above format but show an Internal Content Page – Listing Sections such as Restaurants (this must also include filter categories)

Deliverable 6: Follow the above format but show an Internal Content Page – Top 10 Experiences – this incorporates address and contact details, photo and sub-text

Deliverable 7: The Membership Landing Page which should include:
1. Intro
2. Advertising & Sponsorship Space
3. The four sections
4. Tips Section
Updates

Hi all - just to reiterate that we are open to different approaches in the design.  We only included the existing screen shots of the beta site to provide you with an idea of the content.  We definitely don't want to see anything similar.....we want it to be edgy yet simple and easy to navigate....we want to create an outstanding user experience!  Cheers Tripnook Team

Reason: Dear Designers - We are extending the period as have not had many submissions at all and want to provide more time. If you have already submitted, we will be in touch shortly with feedback. Thanks for your understanding Tripnook Team

Reason: We would like to give everyone more time so we can find the best and most preferred design.

Target Market(s)

TARGET MARKET
tripnook is a consumer focused website, offering a wide-range of easy-to-use and interactive platforms, for informative and commercial purposes, while also providing attractive and innovative advertising real-estate for potential business partners.

The target audience can be segmented as follows:

Primary Target: Professionals travelling on Business

They require up-to-date reliable information prior and during their travel, as well as facilitation to take action. They need an online Personal Assistant.

The personal characteristics of the primary target group are: busy life, tailored solutions, reliable sources, trusting, caring, and spoiled.
 
The website will have a membership option (for a small annual fee) which will provide customized information for their demographic and preferences. Sub target groups will include:
1. Business Men 40 years
3. Business Women 40 years
5. Business People with reduced mobility

Demographic & Travelling Profile of Business Travellers

• 92% of them use the internet as a source of info
• 54% are males, 38 years old
• 80% holds a college/university degree
• 68% is travelling mainly for leisure and annually 6 times per year
• 52% reserve their ticket through the internet
• 66% is travel internationally

Secondary Targets:

Executive PA’s
Executive personal assistants who need to plan their manager’s travel and provide support information for their trip.

Professionals travelling for Leisure and Partners
They have most probably used the website for their business travel, but consider it also useful for their leisure travel. The generic website, will include enough information to cover most of the leisure needs, as well as the requirements of their partners.

Direct Business-to-Business [B2B] Targets
The direct [B2B] targeted audience includes corporations that would like to use a white label solution for their staff, by using all available destinations or a selected number depending on their global network.

Business-to-Business [B2B] Targets
The [B2B] targeted audience is an indirect audience, for which tripnook promotes its services, and a key revenue stream. The B2B audience consists mainly of a diverse range of professional organisations targeting the business traveller (airlines, hotels, travel agencies, tourism authorities, entertainment companies, services, etc.) tripnook will be targeting these organisations to advertise on the site.
 
Desired Response from Target Groups

The desired response from the consumer targets is:
a) Recurrent use of website
b) Share content/experience with friends and social networking sites
c) Interact on the website’s Blog
d) Register for newsletters and offers
e) Subscribe to Membership
f) Be exposed to commercial advertisements on the website
g) Provide feedback (in the future) for services
h) Use (in the future) online services to purchase products and services
Competition

Industry/Entity Type

Travel

Requirements
Must have
• A clean crisp and professional appearance giving a sense of Trust and Reliability.
Should not have
• It should not look like every other run of the mill travel sites - Roomvale.com, Jaunteo etc

```html
<!DOCTYPE html>
<html lang="en">
<head>
<meta charset="utf-8">
<title>tripnook – Global Business Travel</title>
<link href="https://fonts.googleapis.com/css2?family=Roboto+Condensed:wght@400;700&family=Arimo:wght@400;700&display=swap" rel="stylesheet">
<style>
:root{
  --orange:#f47b16;
  --orange-bright:#ff8a00;
  --yellow:#f7b500;
  --black:#0d0d0d;
  --ink:#333;
  --text:#555;
  --grey-dark:#4a4a4a;
  --white:#fff;
  --cond:"Roboto Condensed",Arial,sans-serif;
  --body:"Arimo",Arial,sans-serif;
}
*{margin:0;padding:0;box-sizing:border-box}
html,body{width:750px;height:1200px;overflow:hidden}
body{position:relative;background:var(--white);font-family:var(--body);color:var(--text)}
.abs{position:absolute}

.topbar{left:0;top:0;width:750px;height:34px;background:var(--black)}
.callus{right:193px;top:11px;font:700 10px var(--cond);color:#fff;white-space:nowrap}
.callus span{color:var(--orange-bright)}
.top-search{left:570px;top:7px;width:144px;height:20px;background:#fff;border-radius:2px;font-size:10px;color:#999;padding:4px 6px}
.top-search svg{position:absolute;right:5px;top:3px}

.header{left:0;top:34px;width:750px;height:59px;border-bottom:1px solid #ddd}
.logo{left:34px;top:48px;display:flex;align-items:center;gap:8px}
.logo-mark{width:30px;height:30px;background:var(--orange);border-radius:50%}
.logo-name{font:700 32px var(--body);color:var(--orange);letter-spacing:-.5px}
.nav{right:107px;top:57px;display:flex;gap:14px;font:400 14px var(--cond);color:var(--ink);white-space:nowrap}
.nav .active{color:var(--orange)}
.login{left:658px;top:54px;width:55px;height:20px;background:var(--yellow);border:1px solid #e09a00;border-radius:2px;font:400 11px var(--body);color:#333;text-align:center;line-height:18px}

.hero{left:0;top:93px;width:750px;height:387px;background:linear-gradient(180deg,#6b7079 0%,#9aa2aa 45%,#8a8f7f 70%,#4d5a46 100%)}
.finder{left:37px;top:110px;width:186px;height:182px;background:var(--black);border:2px solid #555;padding:13px 13px}
.finder h3{font:400 10px var(--body);color:#fff;margin-bottom:8px}
.radios{display:flex;gap:14px;font-size:10px;color:#ddd;margin-bottom:10px}
.radios i{display:inline-block;width:8px;height:8px;border-radius:50%;background:#888;margin-right:5px;vertical-align:-1px}
.radios .on i{background:var(--orange)}
.field{height:19px;background:#fff;font-size:9px;color:#999;padding:4px 7px;margin-bottom:13px}
.date{display:flex;width:103px;margin-bottom:13px}
.date .field{width:67px;margin:0}
.date .cal{width:36px;height:19px;background:#fff;border-left:1px solid #ccc;display:flex;align-items:center;justify-content:center}
.finder .go{height:21px;background:var(--orange);color:#fff;font-size:9px;text-align:center;line-height:21px}
.about{right:37px;top:321px;display:flex;flex-direction:column;align-items:flex-end;gap:9px;font:700 13px var(--cond);color:#fff}
.about div{background:rgba(0,0,0,.55);padding:3px 6px}
.about .title{font-size:20px;padding:2px 6px}
.about em{font-style:normal;color:var(--orange-bright)}

.servicebar{left:0;top:480px;width:750px;height:34px;background:var(--orange);display:flex;justify-content:center;align-items:center;gap:24px;font:400 11px var(--body);color:#fff}
.servicebar span{display:flex;align-items:center;gap:6px}

.section-title{font:400 15px var(--cond);color:var(--orange)}
.offer-title{left:34px;top:532px}
.offer{top:552px;width:217px;height:153px}
.offer .photo{width:100%;height:100%}
.offer .cap{position:absolute;left:0;bottom:0;width:100%;height:27px;background:rgba(0,0,0,.75);font:400 13px var(--cond);color:#fff;text-align:center;line-height:27px}
.offer .cap em{font-style:normal;color:var(--orange-bright)}

.howto-title{left:34px;top:724px}
.howto{left:34px;top:748px;width:436px;font-size:8.4px;line-height:14.3px;color:var(--text)}
.howto p{margin-bottom:7px}
.video{left:495px;top:727px;width:219px;height:176px;border:1px solid #ccc;background:#fff;padding:7px}
.video .screen{width:100%;height:100%;background:linear-gradient(180deg,#6fb8e0,#3d8fc0);position:relative}
.video .play{position:absolute;left:50%;top:50%;width:50px;height:50px;margin:-25px 0 0 -25px;background:#fff;border-radius:50%}

.lower{left:0;top:925px;width:750px;height:227px;background:var(--grey-dark)}
.col-title{font:400 14px var(--cond);color:#e5e5e5;top:943px}
.blog-item{position:absolute;left:34px;width:217px;display:flex;gap:10px;padding-bottom:17px;border-bottom:1px solid #666}
.datebox{width:29px;height:30px;background:#2a2a2a;color:var(--orange);font-size:8px;text-align:center;line-height:10px;padding-top:5px;flex:none}
.blog-item p,.news-item p{font-size:8.4px;line-height:12px;color:#ddd}
.news-item{position:absolute;left:299px;width:217px;display:flex;gap:7px;padding-bottom:12px;border-bottom:1px solid #666}
.thumb{width:29px;height:31px;flex:none;background:linear-gradient(135deg,#c9a58a,#7a5a48)}
.social{top:979px;width:38px;height:38px;border-radius:4px;font:700 7px var(--body);color:#fff;display:flex;align-items:center;justify-content:center}
.fan{left:564px;top:1043px;display:flex;gap:12px;align-items:center}
.fan-mark{width:48px;height:48px;background:#fff}
.fan-name{font:700 15px var(--body);color:#ddd}
.like{display:flex;align-items:center;gap:6px;margin-top:7px;font-size:10px;color:#fff}
.like b{background:#eef;color:#3b5998;font:400 7px var(--body);padding:3px 5px;border:1px solid #99a}

.footer{left:0;top:1152px;width:750px;height:48px;background:var(--black);text-align:center;font-size:9px;color:#ccc;padding-top:12px;line-height:14px}
.footer a{color:#ccc;text-decoration:none}
.footer .active{color:var(--orange)}
</style>
</head>
<body>

<div class="abs topbar"></div>
<div class="abs callus">Call us : <span>+65 5550 1827</span></div>
<div class="abs top-search">Search
  <svg width="13" height="13" viewBox="0 0 13 13"><circle cx="5.5" cy="5.5" r="4" fill="none" stroke="#999" stroke-width="1.6"/><line x1="8.5" y1="8.5" x2="12" y2="12" stroke="#999" stroke-width="2"/></svg>
</div>

<div class="abs header"></div>
<div class="abs logo"><span class="logo-mark"></span><span class="logo-name">tripnook</span></div>
<nav class="abs nav"><span class="active">Home</span><span>General</span><span>Business</span><span>Leisure</span><span>Personal</span><span>Contact</span></nav>
<div class="abs login">Login</div>

<div class="abs hero" role="img" aria-label="City skyline with glass towers, a stone bridge and river under cloudy sky"></div>
<div class="abs finder">
  <h3>Find the perfect trip</h3>
  <div class="radios"><span class="on"><i></i>Hotels</span><span><i></i>Destinations</span></div>
  <div class="field">City or Hotel Name</div>
  <div class="date"><div class="field">Check - in</div><div class="cal"><svg width="8" height="8"><g fill="#333"><rect x="0" y="0" width="2" height="2"/><rect x="3" y="0" width="2" height="2"/><rect x="6" y="0" width="2" height="2"/><rect x="0" y="3" width="2" height="2"/><rect x="3" y="3" width="2" height="2"/><rect x="6" y="3" width="2" height="2"/><rect x="0" y="6" width="2" height="2"/><rect x="3" y="6" width="2" height="2"/><rect x="6" y="6" width="2" height="2"/></g></svg></div></div>
  <div class="date"><div class="field">Check - out</div><div class="cal"><svg width="8" height="8"><g fill="#333"><rect x="0" y="0" width="2" height="2"/><rect x="3" y="0" width="2" height="2"/><rect x="6" y="0" width="2" height="2"/><rect x="0" y="3" width="2" height="2"/><rect x="3" y="3" width="2" height="2"/><rect x="6" y="3" width="2" height="2"/><rect x="0" y="6" width="2" height="2"/><rect x="3" y="6" width="2" height="2"/><rect x="6" y="6" width="2" height="2"/></g></svg></div></div>
  <div class="go">Search</div>
</div>
<div class="abs about">
  <div class="title">About</div>
  <div><em>Tripnook</em> is the first <em>Global Business Travel</em></div>
  <div>Website that Provides the most comprehensive</div>
  <div>Destination information tailored to suit the <em>Corporate traveller.</em></div>
</div>

<div class="abs servicebar">
  <span><svg width="12" height="12" viewBox="0 0 12 12"><circle cx="7.5" cy="4.5" r="3.5" fill="none" stroke="#333" stroke-width="1.5"/><line x1="5" y1="7" x2="1" y2="11" stroke="#333" stroke-width="2"/></svg>Booking</span>
  <span><svg width="14" height="12" viewBox="0 0 14 12"><path d="M1 11 L13 1 M4 4 L9 5 M6 9 L7 5" stroke="#333" stroke-width="2" fill="none"/></svg>Flights</span>
  <span><svg width="16" height="16" viewBox="0 0 16 16"><rect x="1" y="5" width="7" height="11" fill="#333"/><rect x="8" y="1" width="7" height="15" fill="#555"/></svg>Hotels</span>
  <span><svg width="16" height="14" viewBox="0 0 16 14"><path d="M1 7 L8 1 H15 V8 L8 14 Z" fill="#333"/></svg>Deals</span>
</div>

<h2 class="abs section-title offer-title">SPECIAL OFFER</h2>
<div class="abs offer" style="left:34px"><div class="photo" role="img" aria-label="Couple relaxing on a rocky beach" style="background:linear-gradient(180deg,#8e8a84,#d8d2c8)"></div><div class="cap">Beach Getaways - Save up to <em>50%</em></div></div>
<div class="abs offer" style="left:265px"><div class="photo" role="img" aria-label="Traveller in front of a raised bascule bridge" style="background:linear-gradient(180deg,#b9c6d2,#6e7a82)"></div><div class="cap">International Deals - Save up to <em>45%</em></div></div>
<div class="abs offer" style="left:496px"><div class="photo" role="img" aria-label="Woman reading a map beside a river with an iron tower in the distance" style="background:linear-gradient(180deg,#a9c4e0,#5e7a6a)"></div><div class="cap">Luxurious Escapes - Save up to <em>50%</em></div></div>

<h2 class="abs section-title howto-title">HOW TO USE</h2>
<div class="abs howto">
  <p>Lorem ipsum dolor sit amet, consectetur adipiscing elit. Donec nec dignissim lorem. Vestibulum odio ante, malesuada ac auctor vitae, mollis tempus dolor. Praesent tincidunt felis eget dui consequat consectetur. Maecenas enim ipsum, vulputate sit amet posuere et, rutrum at neque. Morbi suscipit justo tellus, eu dictum metus ultrices nec.Suspendisse at ipsum suscipit nunc placerat porttitor.</p>
  <p>Integer eget lobortis nulla. Etiam scelerisque neque et cursus vehicula. Sed sed lobortis ante, sed commodo eros. Fusce eget dictum tellus. Nam at nulla laoreet, fringilla mi id, fringilla felis. Curabitur blandit, libero vitae scelerisque sollicitudin, lorem magna molestie magna, vel tempor velit lorem vel leo.</p>
  <p>Duis odio tortor, elementum ac nibh in, varius vehicula risus.Nam tristique accumsan porttitor. Integer erat sapien, venenatis eu commodo vel, eleifend a dolor. In cursus quis ipsum sit amet auctor. In non convallis risus. Aliquam tempor felis tristique diam pharetra malesuada.Proin rhoncus lacinia erat quis feugiat.</p>
</div>
<div class="abs video"><div class="screen" role="img" aria-label="Video still of a dolphin playing with a ball in a pool"><div class="play"><svg width="50" height="50" viewBox="0 0 50 50"><path d="M20 14 L36 25 L20 36 Z" fill="#333"/></svg></div></div></div>

<div class="abs lower"></div>
<h2 class="abs col-title" style="left:34px">LATEST BIOG</h2>
<h2 class="abs col-title" style="left:299px">NEWS FEEDS</h2>
<h2 class="abs col-title" style="left:564px">FOLLOW US</h2>

<div class="blog-item" style="top:970px"><div class="datebox">16<br>JUL</div><p>Lorem ipsum dolor sit amet, consectetur rem ipsum dolor sit amet, Miscing elit. Donec nec</p></div>
<div class="blog-item" style="top:1028px"><div class="datebox">16<br>JUL</div><p>Lorem ipsum dolor sit amet, consectetur rem ipsum dolor sit amet, Miscing elit. Donec nec</p></div>
<div class="blog-item" style="top:1086px"><div class="datebox">16<br>JUL</div><p>Lorem ipsum dolor sit amet, consectetur rem ipsum dolor sit amet, Miscing elit. Donec nec</p></div>

<div class="news-item" style="top:968px"><div class="thumb" role="img" aria-label="News photo"></div><p>Lorem ipsum dolor sit amet, consectetur scin g elit. Donec nec dignissim lorem. tempor velit lorem vel leo. Duis odio tortor</p></div>
<div class="news-item" style="top:1028px"><div class="thumb" role="img" aria-label="News photo"></div><p>Lorem ipsum dolor sit amet, consectetur scing elit. Donec nec dignissim lorem.</p></div>
<div class="news-item" style="top:1086px"><div class="thumb" role="img" aria-label="News photo"></div><p>Lorem ipsum dolor sit amet, consectetur cing elit. Donec nec dignissim lorem.</p></div>

<div class="abs social" style="left:583px;background:#3f6bbf">Chatterly</div>
<div class="abs social" style="left:652px;background:#3a5068">Scrollbin</div>
<div class="abs fan">
  <div class="fan-mark" role="img" aria-label="tripnook"></div>
  <div><div class="fan-name">tripnook</div><div class="like"><b>Like</b>125 like</div></div>
</div>

<footer class="abs footer">
  <a class="active">Home</a> &nbsp;|&nbsp; <a>General</a> &nbsp;|&nbsp; <a>Business</a> &nbsp;|&nbsp; <a>Lesiure</a> &nbsp;|&nbsp; <a>Personal</a> &nbsp;|&nbsp; <a>Contact</a><br>
  Copyright © All rights reserved, 2013
</footer>

</body>
</html>
```